Food broker, trader, wholesaler, liquidator looking for a 5 pages website

Looking for a 5 pages website design. We are food brokers, traders, wholesaler and closeout buyer working with manufacturers, distributors, importers sell to retailers, food service operators and industrial (ingredients). We help market their products. We are a resource for those who need a solution in the distribution/selling/placement of food on the shelves, kitchens and pantries. Whether we open new accounts with new products or sell short dated inventory, we know where to go and get results.

Target Market(s)

Food manufacturers, food distributors, food brokers

Coding

Coded - Design and coding required

Number of Pages Required

4 page

Font styles to use
Serif

Requirements
Must have
• Food-food production-warehouse-Food packaging-people meeting-trucks-supermarket shelves-

```html
<!DOCTYPE html>
<html lang="en">
<head>
<meta charset="utf-8">
<title>Harborline Provisions – Food Brokers, Traders and Wholesaler</title>
<link rel="stylesheet" href="https://fonts.googleapis.com/css2?family=Lexend:wght@300;400;500;600&display=swap">
<style>
:root{
  --navy:#12135e;
  --orange:#f9b233;
  --ink:#3d3d4a;
  --muted:#6b6b78;
  --mist:#e8eef2;
  --white:#ffffff;
}
*{box-sizing:border-box;margin:0;padding:0}
html,body{width:1200px;height:2620px;overflow:hidden;background:var(--white)}
body{position:relative;font-family:"Lexend",sans-serif;color:var(--ink)}
.abs{position:absolute}
.btn{position:absolute;display:flex;align-items:center;justify-content:center;border-radius:16px;font-size:13px;height:32px}
.btn-navy{background:var(--navy);color:var(--white)}
.btn-orange{background:var(--orange);color:var(--navy)}

/* header */
.site-header{position:absolute;left:0;top:0;width:1200px;height:96px;background:var(--white)}
.brand{position:absolute;left:88px;top:30px;display:flex;align-items:center;gap:10px}
.brand-dot{width:36px;height:36px;border-radius:50%;background:var(--navy)}
.brand-name{font-size:15px;font-weight:600;color:var(--navy)}
.nav a{position:absolute;top:40px;font-size:13px;color:var(--ink);text-decoration:none}
.nav .active{color:var(--orange)}
.call{position:absolute;left:768px;top:39px;font-size:14px;color:var(--orange);display:flex;align-items:center;gap:6px}
.call b{color:var(--navy);font-weight:500}

/* hero */
.hero{position:absolute;left:0;top:96px;width:1200px;height:544px;background:linear-gradient(110deg,#b9a79a 0%,#d9d3cc 35%,#c9c4c2 60%,#8d7461 100%)}
.hero-shade{position:absolute;inset:0;background:linear-gradient(90deg,rgba(30,25,30,.45),rgba(30,25,30,0) 60%)}
.hero h1{position:absolute;left:88px;top:168px;font-size:30px;line-height:36px;font-weight:500;color:var(--white);width:440px}
.hero p{position:absolute;left:88px;top:252px;width:440px;font-size:14px;line-height:19px;font-weight:500;color:var(--white)}
.slide-arrow{position:absolute;left:1080px;width:32px;height:32px;border-radius:50%;display:flex;align-items:center;justify-content:center}
.badge{position:absolute;left:552px;top:592px;width:96px;height:80px;border-radius:50%;background:var(--navy);border:5px solid var(--white)}

/* services */
.section-title{position:absolute;font-size:28px;font-weight:500;color:var(--navy)}
.card-img{position:absolute;top:773px;width:320px;height:202px;border-bottom:3px solid var(--navy)}
.card-corner{position:absolute;top:975px;width:40px;height:38px}
.card h3{position:absolute;top:1003px;font-size:18px;font-weight:500;color:var(--navy)}
.card p{position:absolute;top:1037px;width:270px;font-size:13px;line-height:18px;color:var(--muted)}

/* welcome */
.welcome{position:absolute;left:0;top:1212px;width:1200px;height:456px;background:var(--navy)}
.welcome .kicker{position:absolute;left:616px;top:78px;font-size:14px;color:var(--orange);font-weight:500}
.welcome h2{position:absolute;left:616px;top:96px;font-size:28px;font-weight:500;color:var(--white)}
.welcome p{position:absolute;left:616px;width:500px;font-size:13px;line-height:19px;color:var(--white)}
.welcome p.lead{font-weight:600}

/* why */
.why p{position:absolute;left:88px;width:480px;font-size:13px;line-height:19px;color:var(--muted)}
.feature-ring{position:absolute;top:2009px;width:80px;height:80px;border-radius:50%;border:2px solid var(--orange);display:flex;align-items:center;justify-content:center}
.feature-label{position:absolute;top:2101px;font-size:15px;font-weight:500;color:var(--navy)}

/* quote */
.quote{position:absolute;left:736px;top:1748px;width:376px;height:464px;background:var(--mist)}
.quote-dot{position:absolute;left:158px;top:-20px;width:60px;height:46px;border-radius:50%;background:var(--navy);border:3px solid var(--white)}
.quote h3{position:absolute;left:0;width:376px;top:46px;text-align:center;font-size:18px;font-weight:500;color:var(--navy)}
.field{position:absolute;left:32px;width:312px;height:32px;background:var(--white);border-radius:16px;font-size:11px;color:var(--muted);padding:9px 22px}
.field.area{height:96px;border-radius:18px}
.field.select{display:flex;justify-content:space-between;align-items:center;padding-top:0;padding-bottom:0}

/* footer */
.footer{position:absolute;left:0;top:2300px;width:1200px;height:320px;background:var(--mist)}
.footer .logo-dot{position:absolute;left:88px;top:64px;width:88px;height:66px;border-radius:50%;background:var(--navy)}
.footer h4{position:absolute;top:80px;font-size:16px;font-weight:500;color:var(--navy)}
.footer .small{position:absolute;font-size:13px;color:var(--muted);line-height:19px}
.footer .links a{position:absolute;left:583px;font-size:12px;color:var(--muted);text-decoration:none}
.social{position:absolute;top:2448px;width:32px;height:32px;border-radius:50%;border:1px solid var(--orange)}
</style>
</head>
<body>

<header class="site-header">
  <div class="brand"><span class="brand-dot"></span><span class="brand-name">Harborline Provisions</span></div>
  <nav class="nav">
    <a class="active" style="left:342px">-- Home --</a>
    <a style="left:446px">About Us</a>
    <a style="left:540px">What We Do</a>
    <a style="left:656px">Contact Us</a>
  </nav>
  <div class="call">Call Us:
    <svg width="16" height="16" viewBox="0 0 24 24" fill="none" stroke="#f9b233" stroke-width="2"><path d="M22 16.9v3a2 2 0 0 1-2.2 2 19.8 19.8 0 0 1-8.6-3.1 19.5 19.5 0 0 1-6-6A19.8 19.8 0 0 1 2.1 4.2 2 2 0 0 1 4.1 2h3a2 2 0 0 1 2 1.7c.1 1 .4 1.9.7 2.8a2 2 0 0 1-.5 2.1L8 9.9a16 16 0 0 0 6 6l1.3-1.3a2 2 0 0 1 2.1-.4c.9.3 1.8.6 2.8.7a2 2 0 0 1 1.7 2z"/></svg>
    <b>555-018-2460</b></div>
  <div class="btn btn-navy" style="left:984px;top:32px;width:128px">Giving Back</div>
</header>

<section class="hero" role="img" aria-label="Food production staff in hairnets and gloves packing baked goods in a bakery">
  <div class="hero-shade"></div>
  <h1>We are Food Brokers, Traders and Wholesaler</h1>
  <p>Closeout buyer working with manufacturers, distributors, importers sell to retailers, food service operators and industrial (ingredients).</p>
  <div class="btn btn-orange" style="left:88px;top:336px;width:128px">Contact Us</div>
  <div class="slide-arrow" style="top:237px;background:rgba(255,255,255,.6)">
    <svg width="10" height="10" viewBox="0 0 10 10"><path d="M6.5 1.5 3 5l3.5 3.5" fill="none" stroke="#12135e" stroke-width="1.4"/></svg></div>
  <div class="slide-arrow" style="top:276px;background:var(--orange)">
    <svg width="10" height="10" viewBox="0 0 10 10"><path d="M3.5 1.5 7 5 3.5 8.5" fill="none" stroke="#12135e" stroke-width="1.4"/></svg></div>
</section>
<div class="badge"></div>

<h2 class="section-title" style="left:0;width:1200px;text-align:center;top:705px">What We Do</h2>

<article class="card">
  <div class="card-img" style="left:88px;background:linear-gradient(135deg,#c7b7a5,#8e7058)" role="img" aria-label="Two shop staff in aprons smiling in a bakery store"></div>
  <div class="card-corner" style="left:368px;background:#9a6a4a"></div>
  <h3 style="left:112px">Sales &amp; Marketing</h3>
  <p style="left:112px">We connect food buyers and sellers through a dedicated approach.</p>
  <div class="btn btn-navy" style="left:112px;top:1100px;width:80px">More</div>
</article>
<article class="card">
  <div class="card-img" style="left:440px;background:linear-gradient(135deg,#8fa9b8,#b07a4a 55%,#4f7c96)" role="img" aria-label="Aerial view of a cargo ship loaded with containers at a port"></div>
  <div class="card-corner" style="left:720px;background:#3d6e8c"></div>
  <h3 style="left:464px">Trading</h3>
  <p style="left:464px">We purchase goods anywhere and ship them Nationwide and Export.</p>
  <div class="btn btn-orange" style="left:464px;top:1100px;width:80px">More</div>
</article>
<article class="card">
  <div class="card-img" style="left:792px;background:linear-gradient(135deg,#d6c7b5,#c0503a 50%,#5a78a8)" role="img" aria-label="Supermarket aisle with stocked shelves"></div>
  <div class="card-corner" style="left:1072px;background:#c85a3c"></div>
  <h3 style="left:816px">Closeout/Excess Inventory</h3>
  <p style="left:816px">we buy closeouts and excess inventory for prisons, outlet stores and discounters.</p>
  <div class="btn btn-navy" style="left:816px;top:1100px;width:80px">More</div>
</article>

<section class="welcome">
  <svg class="abs" style="left:0;top:0" width="530" height="456" viewBox="0 0 530 456">
    <defs><linearGradient id="wh" x1="0" y1="0" x2="1" y2="1"><stop offset="0" stop-color="#d8dde0"/><stop offset=".5" stop-color="#c49070"/><stop offset="1" stop-color="#9a9fa3"/></linearGradient></defs>
    <polygon points="0,0 394,0 528,228 394,456 0,456" fill="#f9b233"/>
    <polygon points="0,0 380,0 514,228 380,456 0,456" fill="url(#wh)" role="img" aria-label="Warehouse interior with pallet racking and boxed food stock"/>
  </svg>
  <div class="kicker">Welcome to</div>
  <h2>Harborline Provisions</h2>
  <p class="lead" style="top:144px">Harborline Provisions works with food manufacturers, brand owners, distributors and wholesalers market their products.</p>
  <p class="lead" style="top:202px">Retail, Food Service and Industrial ingredients.</p>
  <p style="top:240px">Founded in 2008, Harborline Provisions started with the distribution of gluten free products understanding the need to provide access to unique flavors and products for the celiac consumers. From this, we expanded into deli, dairy, groceries, frozen and beverages.</p>
  <div class="btn btn-orange" style="left:616px;top:343px;width:128px">About Us</div>
</section>

<section class="why">
  <h2 class="section-title" style="left:88px;top:1833px">Why Choose Us</h2>
  <p style="top:1885px">We pride ourselves in working in an easy, personal and accessible environment making our customers and vendors comfortable with us.</p>
  <p style="top:1943px">We look forward to connecting with you and evaluating how we can assist you reaching your sales objectives.</p>
  <div class="feature-ring" style="left:101px">
    <svg width="30" height="30" viewBox="0 0 24 24" fill="none" stroke="#12135e" stroke-width="1.6"><path d="M4 13h16l-2 7H6z"/><path d="M7 13V8h10v5"/><path d="M12 4v4"/><path d="M10 4h4"/></svg></div>
  <div class="feature-label" style="left:88px">Supply Security</div>
  <div class="feature-ring" style="left:276px">
    <svg width="30" height="30" viewBox="0 0 24 24" fill="none" stroke="#12135e" stroke-width="1.6"><path d="M12 2v20"/><path d="M17 6H9.5a3.5 3.5 0 0 0 0 7h5a3.5 3.5 0 0 1 0 7H6"/></svg></div>
  <div class="feature-label" style="left:245px">Competitive Pricing</div>
  <div class="feature-ring" style="left:455px">
    <svg width="28" height="28" viewBox="0 0 24 24" fill="none" stroke="#12135e" stroke-width="1.6"><path d="M4 16v-4a8 8 0 0 1 16 0v4"/><rect x="3" y="14" width="4" height="6" rx="1"/><rect x="17" y="14" width="4" height="6" rx="1"/></svg></div>
  <div class="feature-label" style="left:424px">Customer Focussed</div>
</section>

<aside class="quote">
  <div class="quote-dot"></div>
  <h3>Request a Quote</h3>
  <div class="field" style="top:86px">Enter Your Name</div>
  <div class="field" style="top:134px">Phone</div>
  <div class="field" style="top:182px">Email</div>
  <div class="field select" style="top:230px">Choose a Service
    <svg width="10" height="10" viewBox="0 0 10 10"><path d="M2 3.5 5 6.5 8 3.5" fill="none" stroke="#6b6b78" stroke-width="1.2"/></svg></div>
  <div class="field area" style="top:278px">Message ...</div>
  <div class="btn btn-orange" style="left:32px;top:390px;width:312px">Send Us Message</div>
</aside>

<footer class="footer">
  <div class="logo-dot"></div>
  <h4 style="left:208px">Harborline Provisions</h4>
  <div class="abs" style="left:208px;top:130px;font-size:18px;color:var(--orange);display:flex;align-items:center;gap:6px">Call Us:
    <svg width="18" height="18" viewBox="0 0 24 24" fill="none" stroke="#f9b233" stroke-width="2"><path d="M22 16.9v3a2 2 0 0 1-2.2 2 19.8 19.8 0 0 1-8.6-3.1 19.5 19.5 0 0 1-6-6A19.8 19.8 0 0 1 2.1 4.2 2 2 0 0 1 4.1 2h3a2 2 0 0 1 2 1.7c.1 1 .4 1.9.7 2.8a2 2 0 0 1-.5 2.1L8 9.9a16 16 0 0 0 6 6l1.3-1.3a2 2 0 0 1 2.1-.4c.9.3 1.8.6 2.8.7a2 2 0 0 1 1.7 2z"/></svg>
    <span style="color:var(--navy)">555-018-2471</span></div>
  <div class="small" style="left:208px;top:154px">e. support@harborlineprovisions.com</div>
  <div class="small" style="left:208px;top:190px;color:var(--orange);font-size:12px">Location:</div>
  <div class="small" style="left:208px;top:208px;width:260px">4410 Cedar Harbor Ave Lakeport,<br>WN 48210</div>

  <h4 style="left:583px">Quick Links</h4>
  <div class="links">
    <a style="top:111px">Home</a>
    <a style="top:135px">About Us</a>
    <a style="top:159px">What We Do</a>
    <a style="top:183px">Contact Us</a>
    <a style="top:207px">Giving Back</a>
  </div>

  <h4 style="left:815px">© 2020 Harborline Provisions</h4>
  <div class="small" style="left:815px;top:110px">All Rights Reserved.</div>

  <svg class="abs" style="left:1098px;top:85px" width="30" height="36" viewBox="0 0 30 36"><path d="M15 2 3 34 15 26 27 34Z" fill="none" stroke="#f9b233" stroke-width="2" stroke-linejoin="round"/></svg>
</footer>
<div class="social" style="left:816px"></div>
<div class="social" style="left:856px;background:var(--orange)"></div>
<div class="social" style="left:896px"></div>
<div class="social" style="left:936px"></div>

</body>
</html>
```